Tallwater Marketing Business Card

Business card using new logo for marketing consulting company based in Silicon Valley. Limited information on card now (name, phone number, email, website), but room to add mailing address later.

```html
<!DOCTYPE html>
<html lang="en">
<head>
<meta charset="utf-8">
<title>Tallwater Marketing Business Card</title>
<link href="https://fonts.googleapis.com/css2?family=Roboto:wght@400;500;700&display=swap" rel="stylesheet">
<style>
  :root {
    --page: #ecebe8;
    --card: #ffffff;
    --brand-blue: #29abe2;
    --deep-blue: #1b75bc;
    --violet: #4b3c9e;
    --ink: #333333;
    --muted: #555555;
    --contact-ink: #2e3a7a;
    --shadow: rgba(0,0,0,0.18);
  }
  * { box-sizing: border-box; margin: 0; padding: 0; }
  html, body {
    width: 1200px; height: 913px; overflow: hidden;
    background: var(--page);
    font-family: "Roboto", Arial, sans-serif;
  }
  .canvas { position: relative; width: 1200px; height: 913px; }
  .card {
    position: absolute; width: 525px; height: 300px;
    background: var(--card);
    box-shadow: 0 6px 18px var(--shadow);
    overflow: hidden;
  }
  .card-front { left: 50px; top: 306px; }
  .card-back { left: 625px; top: 306px; }

  .wordmark {
    font-weight: 400; color: var(--brand-blue);
    text-transform: uppercase; line-height: 1.1; white-space: nowrap;
  }
  .card-front .wordmark {
    position: absolute; left: 0; right: 0; top: 122px;
    text-align: center; font-size: 30px; letter-spacing: 1px;
  }

  .back-bands { position: absolute; inset: 0; width: 100%; height: 100%; }

  .card-back .wordmark {
    position: absolute; left: 30px; top: 130px;
    font-size: 19px; letter-spacing: 0.4px;
  }
  .person {
    position: absolute; left: 120px; top: 168px;
    display: flex; align-items: baseline; gap: 8px;
  }
  .person-name { font-size: 16px; font-weight: 700; color: var(--ink); }
  .person-title { font-size: 11px; color: var(--muted); }

  .contact-list {
    position: absolute; left: 300px; top: 88px; list-style: none;
  }
  .contact-list li {
    display: flex; align-items: center; gap: 7px;
    font-size: 10.5px; color: var(--contact-ink); height: 17px; white-space: nowrap;
  }
  .contact-list svg { width: 11px; height: 11px; fill: var(--deep-blue); flex: none; }
  .contact-list .web { font-weight: 700; }
  .contact-list .web .domain { color: var(--brand-blue); }
</style>
</head>
<body>
<main class="canvas">
  <section class="card card-front" aria-label="Business card front">
    <p class="wordmark">Tallwater Marketing</p>
  </section>

  <section class="card card-back" aria-label="Business card back">
    <svg class="back-bands" viewBox="0 0 525 300" preserveAspectRatio="none" aria-hidden="true">
      <path d="M200 0 L525 0 L525 10 C420 8 320 6 200 0 Z" fill="var(--violet)"/>
      <path d="M300 0 L525 0 L525 5 C450 4 380 2 300 0 Z" fill="var(--brand-blue)"/>
      <path d="M0 300 L0 255 C160 275 330 250 525 185 L525 300 Z" fill="var(--deep-blue)"/>
      <path d="M0 300 L0 272 C170 288 340 268 525 215 L525 300 Z" fill="var(--brand-blue)"/>
      <path d="M0 300 L0 288 C190 298 350 280 525 245 L525 300 Z" fill="var(--violet)"/>
    </svg>

    <p class="wordmark">Tallwater Marketing</p>

    <div class="person">
      <p class="person-name">Your Name</p>
      <p class="person-title">Title</p>
    </div>

    <ul class="contact-list">
      <li><svg viewBox="0 0 12 12"><path d="M6 0a4 4 0 0 0-4 4c0 3 4 8 4 8s4-5 4-8a4 4 0 0 0-4-4zm0 5.5A1.5 1.5 0 1 1 6 2.5a1.5 1.5 0 0 1 0 3z"/></svg><span>Your Commercial or office address</span></li>
      <li><svg viewBox="0 0 12 12"><path d="M1 4c0-2 2-3 5-3s5 1 5 3l-2 1-1-2H4L3 5zM2 6h8v5H2z"/></svg><span>00.00.00.0000</span></li>
      <li><svg viewBox="0 0 12 12"><path d="M3 1h6v3H3zM1 5h10v5H9v2H3v-2H1zM4 8v3h4V8z"/></svg><span>00.00.00.0000</span></li>
      <li><svg viewBox="0 0 12 12"><path d="M0 2h12v8H0zM1 3l5 4 5-4v-.1H1z"/></svg><span>yourname@yourwebsite.com</span></li>
      <li class="web"><svg viewBox="0 0 12 12"><path d="M6 0a6 6 0 1 0 0 12A6 6 0 0 0 6 0zm0 1c.8 0 1.6 1.6 1.8 4H4.2C4.4 2.6 5.2 1 6 1zM1 6h2.2c0 1.3.3 2.6.7 3.5A5 5 0 0 1 1 6zm3.2 0h3.6c-.2 2.4-1 4-1.8 4S4.4 8.4 4.2 6zm4.6 0H11a5 5 0 0 1-2.9 3.5c.4-.9.7-2.2.7-3.5z"/></svg><span>www.<span class="domain">yourwebsite</span>.com</span></li>
    </ul>
  </section>
</main>
</body>
</html>
```